VORNAK (PTY)LTD Website design

WEBSITE design based on our different divisions in our organization.
Our company specializes in the following.
Construction
Property development
Demolition
Mining
Transport
Manufacturing of concrete bricks and blocks
Lightweight concrete Readymix
I want a very modern website and look that fits in with our organization and the changing times of the world.
The website must be very professional and crisp and should appeal to both the younger generation and older generation of business leaders and.
The website must be very user friendly and easy to navigate, simple yet modern, professional and corporate.

```html
<!DOCTYPE html>
<html lang="en">
<head>
<meta charset="utf-8">
<title>VORNAK (PTY)LTD</title>
<link href="https://fonts.googleapis.com/css2?family=Open+Sans:ital,wght@0,400;0,600;0,700;1,400&display=swap" rel="stylesheet">
<style>
:root{
  --blue:#1ea2d9;
  --blue-dark:#1487ba;
  --navy:#1c2b5a;
  --green:#1aa24a;
  --text:#444b55;
  --muted:#8a9099;
  --grey-bg:#eef1f4;
  --card-bg:#f1f4f7;
  --line:#dde2e7;
  --white:#fff;
}
*{box-sizing:border-box;margin:0;padding:0}
html,body{width:1200px;height:4557px;overflow:hidden}
body{font-family:"Open Sans",Arial,sans-serif;color:var(--text);background:var(--white);position:relative;font-size:14px;line-height:1.6}
.wrap{position:relative;width:1070px;margin:0 auto}
a{color:inherit;text-decoration:none}
.btn{display:inline-block;font-size:12px;font-weight:700;text-transform:uppercase;color:#fff;padding:0 26px;height:44px;line-height:44px}
.btn-green{background:var(--green)}
.btn-blue{background:var(--blue)}
.section-title{font-size:28px;font-weight:700;color:var(--blue);text-transform:uppercase;position:relative;padding-top:28px}
.section-title::before{content:"";position:absolute;left:0;top:0;width:235px;height:3px;background:var(--blue)}

/* top bar */
.topbar{height:30px;background:var(--blue);color:#fff;font-size:12px}
.topbar .wrap{display:flex;justify-content:space-between;align-items:center;height:30px}
.topbar em{font-style:italic}
.topbar-right{display:flex;align-items:center;gap:18px}
.topbar-social{display:flex;gap:14px;margin-left:20px}
.topbar-social span{width:11px;height:11px;border-radius:50%;background:#fff;display:block}

/* header */
.header{height:115px}
.header .wrap{display:flex;align-items:center;height:115px}
.brand{font-size:44px;font-weight:700;color:var(--blue);letter-spacing:1px}
.contact-items{margin-left:auto;display:flex;gap:44px;align-items:center}
.contact-item{display:flex;gap:12px;align-items:center;font-size:13px}
.contact-item small{display:block;color:var(--muted);font-size:12px;line-height:1.3}
.contact-item b{color:var(--blue);font-weight:600}
.header .btn{margin-left:44px;height:48px;line-height:48px}

/* nav */
.nav{height:45px;border-top:1px solid var(--line)}
.nav .wrap{display:flex;align-items:center;height:45px;gap:34px;font-size:13px;font-weight:700;color:#222;text-transform:uppercase}
.nav .search{margin-left:auto}

/* hero */
.hero{position:relative;height:600px;background:linear-gradient(135deg,#3b4a55 0%,#5d6b72 40%,#8a969c 60%,#4c5961 100%)}
.hero-title{position:absolute;left:65px;top:100px;color:#fff;font-size:40px;font-weight:700;line-height:1.3;width:620px}
.hero-sub{position:absolute;left:65px;top:220px;color:#fff;font-size:16px}
.hero-actions{position:absolute;left:65px;top:300px;display:flex;gap:20px}
.hero-search{position:absolute;right:80px;top:22px;width:170px;height:36px;background:#fff;border:1px solid var(--line);font-size:12px;color:var(--muted);padding:8px 12px}
.hero-arrow{position:absolute;top:290px;width:34px;height:34px;background:#111;display:flex;align-items:center;justify-content:center}
.hero-arrow.left{left:0}.hero-arrow.right{right:0}

/* features */
.features{position:absolute;top:633px;left:65px;display:flex;gap:26px}
.feature{width:340px;height:240px;background:var(--card-bg);border:1px solid var(--line);padding:34px 30px}
.feature h3{color:var(--blue);font-size:17px;font-weight:700;text-transform:uppercase;margin:34px 0 10px}
.feature p{font-size:14px}

/* about */
.about{position:absolute;top:918px;left:0;width:1200px}
.about-lead{position:absolute;left:0;top:130px;font-size:31px;font-weight:700;color:var(--navy);line-height:1.35}
.about-text{position:absolute;left:455px;top:118px;width:615px}
.about-text .intro{font-size:18px;color:var(--blue);line-height:1.55;margin-bottom:16px}
.about-text p{font-size:13px}

/* person */
.person{position:absolute;top:1335px;left:0;width:1200px}
.person-frame{position:absolute;left:0;top:115px;width:340px;height:385px;background:var(--navy)}
.person-photo{position:absolute;left:45px;top:0;width:365px;height:470px;background:linear-gradient(180deg,#d9dde1 0%,#6f7b88 55%,#2a3140 100%)}
.person-tag{position:absolute;left:0;top:465px;background:var(--blue);color:#fff;font-size:12px;padding:8px 20px;text-transform:uppercase}
.person-info{position:absolute;left:455px;top:8px;width:615px}
.person-info h2{font-size:31px;font-weight:400;color:#222}
.person-info .role{font-size:12px;font-weight:700;color:var(--blue);text-transform:uppercase;margin-bottom:22px}
.person-info p{font-size:13px;margin-bottom:16px}
.quote{border-left:3px solid var(--navy);background:var(--grey-bg);padding:20px 22px;font-style:italic;font-size:14px;color:var(--muted);margin-top:30px}

/* services */
.services{position:absolute;top:1970px;left:0;width:1200px;height:735px;background:var(--grey-bg)}
.services .section-title{position:absolute;top:90px;left:65px}
.service-list{position:absolute;top:195px;left:65px;display:flex;gap:26px}
.service{width:340px;height:425px;background:var(--blue);position:relative;color:#fff;text-align:center}
.service-img{height:225px}
.service-icon{position:absolute;left:50%;top:195px;transform:translateX(-50%);width:60px;height:60px;border-radius:50%;background:var(--blue);display:flex;align-items:center;justify-content:center}
.service h3{font-size:14px;font-weight:700;text-transform:uppercase;margin-top:58px}
.service p{font-size:14px;padding:6px 60px}

/* testimonial */
.testimonial{position:absolute;top:2810px;left:0;width:1200px;height:300px}
.avatar{position:absolute;left:155px;top:10px;width:150px;height:150px;border-radius:50%;background:linear-gradient(160deg,#c9a889,#6d5a4e);border:4px solid #eee}
.t-name{position:absolute;left:155px;top:190px;width:150px;text-align:center;font-size:15px;font-weight:700;color:#222}
.t-company{position:absolute;left:155px;top:214px;width:150px;text-align:center;font-size:12px;font-style:italic;color:var(--muted)}
.t-quote{position:absolute;left:345px;top:5px;width:700px;font-size:25px;line-height:1.45;color:#222}
.dots{position:absolute;top:275px;left:0;width:1200px;display:flex;justify-content:center;gap:14px}
.dots span{width:9px;height:9px;border-radius:50%;background:#cfd5db}
.dots span.active{background:var(--blue)}

/* cta */
.cta{position:absolute;top:3175px;left:0;width:1200px;height:315px;background:linear-gradient(180deg,#22a9df,#1793c9);text-align:center;color:#fff}
.cta h2{font-size:24px;font-weight:700;margin-top:80px}
.cta p{font-size:14px;width:680px;margin:12px auto 22px}

/* news */
.news{position:absolute;top:3540px;left:0;width:1200px}
.news .section-title{position:absolute;left:65px;top:0}
.news-list{position:absolute;top:140px;left:65px;display:flex;gap:26px}
.news-item{width:340px}
.news-img{height:215px}
.news-item h4{font-size:14px;font-weight:700;color:var(--blue);margin-top:22px;line-height:1.45}
.news-meta{font-size:12px;color:var(--muted);margin-top:8px;padding-bottom:14px;border-bottom:1px solid var(--line);display:flex;gap:24px}

/* footer */
.footer{position:absolute;top:4150px;left:0;width:1200px;height:320px}
.footer-col{position:absolute;top:0}
.footer h5{font-size:22px;font-weight:700;color:#222;margin-bottom:26px}
.footer p,.footer li{font-size:13px}
.footer ul{list-style:none}
.footer li{margin-bottom:12px}
.footer-social{display:flex;gap:10px;margin-top:34px}
.footer-social span{width:34px;height:34px;border-radius:50%;background:#555}
.subscribe{display:flex;margin-top:20px}
.subscribe span{width:210px;height:34px;border:1px solid var(--line);font-size:12px;color:var(--muted);padding:7px 12px}
.subscribe b{width:34px;height:34px;background:#555;display:flex;align-items:center;justify-content:center}
.bottombar{position:absolute;top:4485px;left:0;width:1200px;height:72px;border-top:1px solid var(--line)}
.bottombar p{position:absolute;left:65px;top:22px;font-size:12px}
.to-top{position:absolute;right:10px;top:36px;width:36px;height:36px;background:#58b37a;display:flex;align-items:center;justify-content:center}
</style>
</head>
<body>

<div class="topbar">
  <div class="wrap">
    <em>We help the world growing since 1985</em>
    <div class="topbar-right">
      <span>Career</span><span>Give Feedback</span><span>Contact Us</span>
      <div class="topbar-social"><span></span><span></span><span></span><span></span></div>
    </div>
  </div>
</div>

<header class="header">
  <div class="wrap">
    <div class="brand">VORNAK</div>
    <div class="contact-items">
      <div class="contact-item">
        <svg width="34" height="26" viewBox="0 0 34 26"><rect x="1" y="1" width="32" height="24" rx="2" fill="var(--navy)"/><path d="M2 3l15 11L32 3" stroke="#fff" stroke-width="2" fill="none"/></svg>
        <div><small>Email Support</small><b>info@vornak.co.za</b></div>
      </div>
      <div class="contact-item">
        <svg width="24" height="32" viewBox="0 0 24 32"><rect x="2" y="1" width="20" height="30" rx="3" fill="var(--navy)"/><rect x="5" y="5" width="14" height="19" fill="#fff"/></svg>
        <div><small>Call Support</small><b>+27 0 (21) 555 0148</b></div>
      </div>
    </div>
    <a class="btn btn-green">Get a Quote</a>
  </div>
</header>

<nav class="nav">
  <div class="wrap">
    <span>Home</span><span>About Us</span><span>Why Choose Us</span><span>Our Services</span><span>Industries</span><span>News</span><span>Contact</span>
    <svg class="search" width="16" height="16" viewBox="0 0 16 16"><circle cx="6.5" cy="6.5" r="5" stroke="#222" stroke-width="2" fill="none"/><path d="M10 10l5 5" stroke="#222" stroke-width="2"/></svg>
  </div>
</nav>

<section class="hero" role="img" aria-label="Photograph of a modern glass transit building with street and lamp posts">
  <div class="hero-search">Type and hit enter</div>
  <h1 class="hero-title">The VORNAK Infrastructure Consulting Firm</h1>
  <p class="hero-sub">Lorem ipsum dolor sit amet, consectetur adipisicing elit, sed do eiusmod</p>
  <div class="hero-actions"><a class="btn btn-green">Learn More</a><a class="btn btn-blue">Contact Us</a></div>
  <div class="hero-arrow left"><svg width="12" height="14"><path d="M9 2L3 7l6 5" stroke="#fff" stroke-width="2" fill="none"/></svg></div>
  <div class="hero-arrow right"><svg width="12" height="14"><path d="M3 2l6 5-6 5" stroke="#fff" stroke-width="2" fill="none"/></svg></div>
</section>

<div class="features">
  <div class="feature">
    <svg width="34" height="34" viewBox="0 0 24 24"><path d="M12 2l3 6.5 7 .8-5.2 4.8 1.5 7L12 17.6 5.7 21l1.5-7L2 9.3l7-.8z" fill="none" stroke="#888" stroke-width="1.4"/></svg>
    <h3>Quality Driven</h3>
    <p>Lorem ipsum dolor sit amet, consectetur adipisicing elit sed do eiusmod tempor.</p>
  </div>
  <div class="feature">
    <svg width="34" height="34" viewBox="0 0 24 24"><path d="M2 12a10 10 0 0 1 20 0z" fill="#888"/><path d="M12 12v7a2 2 0 0 1-4 0" stroke="#888" stroke-width="1.6" fill="none"/></svg>
    <h3>Customer Focused</h3>
    <p>Lorem ipsum dolor sit amet, consectetur adipisicing elit sed do eiusmod tempor.</p>
  </div>
  <div class="feature">
    <svg width="38" height="34" viewBox="0 0 28 24"><circle cx="8" cy="7" r="4" fill="#888"/><circle cx="19" cy="6" r="4.5" fill="#888"/><path d="M1 21a7 7 0 0 1 14 0z M11 21a8 8 0 0 1 16 0z" fill="#888"/></svg>
    <h3>Global Sourcing</h3>
    <p>Lorem ipsum dolor sit amet, consectetur adipisicing elit sed do eiusmod tempor.</p>
  </div>
</div>

<section class="about">
  <div class="wrap">
    <h2 class="section-title">About Us</h2>
    <div class="about-lead">The Vornak<br>Building Tomorrow.</div>
    <div class="about-text">
      <p class="intro">Lorem Ipsum is simply dummy text of the printing and typesetting industry. Lorem Ipsum has been the unknown printer took a galley of type and scrambled</p>
      <p>Lorem Ipsum is simply dummy text of the printing and typesetting industry. Lorem Ipsum has been the unknown printer took a galley of type and scrambled. Lorem Ipsum is simply dummy text of the printing and typesetting industry. Lorem Ipsum has been the unknown printer took a galley of type and scrambled. Lorem Ipsum is simply dummy text of the printing and typesetting industry. Lorem Ipsum has been the unknown printer took a galley of type and scrambled.</p>
    </div>
  </div>
</section>

<section class="person">
  <div class="wrap">
    <div class="person-frame"></div>
    <div class="person-photo" role="img" aria-label="Portrait of the head of operations in a dark suit, arms crossed"></div>
    <div class="person-tag">Head of Operations</div>
    <div class="person-info">
      <h2>Daniel Mercer</h2>
      <div class="role">Head of Operations</div>
      <p>Lorem ipsum dolor sit amet, consectetur adipisicing elit, sed do eiusmod tempor incididunt ut labore et dolore magna aliqua. Ut enim ad minim veniam, quis nostrud exercitation ullamco laboris nisi ut aliquip ex ea commodo consequat. Duis aute irure dolor in reprehenderit in voluptate velit esse cillum dolore eu fugiat nulla pariatur. Excepteur sint occaecat cupidatat non proident, sunt in culpa qui officia deserunt mollit anim id est laborum.</p>
      <p>Duis aute irure dolor in reprehenderit in voluptate velit esse cillum dolore eu fugiat nulla pariatur. Excepteur sint occaecat cupidatat non proident, sunt in culpa qui officia deserunt mollit anim id est laborum.</p>
      <div class="quote">Lorem ipsum dolor sit amet, consectetur adipisicing elit, sed do eiusmod tempor incididunt ut labore et dolore magna aliqua. Ut enim ad minim veniam, quis nostrud exercitation ullamco laboris nisi ut aliquip ex ea commodo consequat. Duis aute irure dolor in reprehenderit.</div>
    </div>
  </div>
</section>

<section class="services">
  <h2 class="section-title">Services</h2>
  <div class="service-list">
    <div class="service">
      <div class="service-img" role="img" aria-label="Construction workers on a site at sunset" style="background:linear-gradient(180deg,#3a4a66,#c7723a 70%,#2b2a30)"></div>
      <div class="service-icon"><svg width="26" height="26" viewBox="0 0 24 24"><circle cx="9" cy="14" r="5" fill="none" stroke="#fff" stroke-width="3" stroke-dasharray="3 2"/><circle cx="17" cy="6" r="3.5" fill="none" stroke="#fff" stroke-width="2.4" stroke-dasharray="2 1.6"/></svg></div>
      <h3>Civil</h3>
      <p>Lorem ipsum dolor sit amet, consectetur adipisicing elit sed</p>
    </div>
    <div class="service">
      <div class="service-img" role="img" aria-label="Mining truck in an open pit quarry" style="background:linear-gradient(180deg,#b8bcc0,#8a857a 50%,#5f5a50)"></div>
      <div class="service-icon"><svg width="24" height="24" viewBox="0 0 24 24"><path d="M4 20C4 9 11 4 21 3c-1 10-6 17-17 17z" fill="#fff"/></svg></div>
      <h3>Mining</h3>
      <p>Lorem ipsum dolor sit amet, consectetur adipisicing elit sed</p>
    </div>
    <div class="service">
      <div class="service-img" role="img" aria-label="Glass skyscrapers seen from below" style="background:linear-gradient(160deg,#dfe6ec,#7d97ad 50%,#3d5870)"></div>
      <div class="service-icon"><svg width="20" height="26" viewBox="0 0 20 26"><path d="M10 1c5 7 8 11 8 15a8 8 0 0 1-16 0c0-4 3-8 8-15z" fill="#fff"/></svg></div>
      <h3>Property Development</h3>
      <p>Lorem ipsum dolor sit amet, consectetur adipisicing elit sed</p>
    </div>
  </div>
</section>

<section class="testimonial">
  <div class="avatar" role="img" aria-label="Portrait photo of the client"></div>
  <div class="t-name">Simon Hale</div>
  <div class="t-company">Northline Ltd</div>
  <p class="t-quote">Lorem Ipsum is simply dummy text of the printing and typesetting industry orem Ipsum has been. Mauris ornare tortor in eleifend blanditullam ut ligula et neque. Nulla interdum dapibus erat nec elementum.</p>
  <div class="dots"><span></span><span></span><span></span><span class="active"></span></div>
</section>

<section class="cta">
  <h2>If you need industrial solution... We are available for you</h2>
  <p>We provide innovative solutions for sustainable progress. Our professional team works to increase productivity and cost effectiveness on the market</p>
  <a class="btn btn-green">Contact Us</a>
</section>

<section class="news">
  <h2 class="section-title">Recent News</h2>
  <div class="news-list">
    <div class="news-item">
      <div class="news-img" role="img" aria-label="Desk with laptop, notebooks and coffee" style="background:linear-gradient(135deg,#6b4a36,#a98565 50%,#d7d4d0)"></div>
      <h4>The Best in dolor sit amet consectetur adipisicing elit sed</h4>
      <div class="news-meta"><span>Aug 24, 2017</span><span>0 Comments</span></div>
    </div>
    <div class="news-item">
      <div class="news-img" role="img" aria-label="Stacks of coins on a dark surface" style="background:linear-gradient(135deg,#1d1f22,#4a4538 50%,#9b8a5a)"></div>
      <h4>The Best in dolor sit amet consectetur adipisicing elit sed</h4>
      <div class="news-meta"><span>Aug 24, 2017</span><span>0 Comments</span></div>
    </div>
    <div class="news-item">
      <div class="news-img" role="img" aria-label="Desk with laptop, notebooks and coffee" style="background:linear-gradient(135deg,#6b4a36,#a98565 50%,#d7d4d0)"></div>
      <h4>The Best in dolor sit amet consectetur adipisicing elit sed</h4>
      <div class="news-meta"><span>Aug 24, 2017</span><span>0 Comments</span></div>
    </div>
  </div>
</section>

<footer class="footer">
  <div class="footer-col" style="left:65px;width:340px">
    <div class="brand" style="margin-bottom:22px">VORNAK</div>
    <p>Lorem Ipsum is simply dummy text of the printing and typesetting industry. Lorem Ipsum has been the unknown printer took a galley of type and scrambled.</p>
    <div class="footer-social"><span></span><span></span><span></span><span></span></div>
  </div>
  <div class="footer-col" style="left:432px">
    <h5>Quick Link</h5>
    <ul><li>Home</li><li>About Us</li><li>Multimedia</li><li>Latest News</li><li>Contact Us</li></ul>
  </div>
  <div class="footer-col" style="left:615px;width:230px">
    <h5>Get In Touch</h5>
    <ul><li>P.O. Box 1380 Lorem XYZ NSW 87125</li><li>hello@vornak.co.za</li><li>+27 0 (21) 555 0148</li></ul>
  </div>
  <div class="footer-col" style="left:888px;width:250px">
    <h5>Subscribe</h5>
    <p>Lit sed The Best in dolor sit amet consectetur adipisicing elit sedconsectetur adipisicing</p>
    <div class="subscribe"><span>enter your email</span><b><svg width="14" height="12"><path d="M1 6h11M8 2l4 4-4 4" stroke="#fff" stroke-width="2" fill="none"/></svg></b></div>
  </div>
</footer>

<div class="bottombar">
  <p>© 2018 - All Rights Reserved</p>
  <div class="to-top"><svg width="14" height="10"><path d="M2 8l5-5 5 5" stroke="#fff" stroke-width="2" fill="none"/></svg></div>
</div>

</body>
</html>
```